AUSTRALIAN CONSULTING FIRM BUSINESS CARD - MODERN

We are wanting a modern, clean lined business card design. We are professional niche consultancy firm situated in Australia called Marlow Advisory Partners Pty Ltd.
The card should communicate professionalism and creativity and draw on our logo design (attached).
The design should be two sided, landscape orientation.
Target Market(s)
government, not for profit sector, corporate clients
Industry/Entity Type
Landscape
Requirements
Must have
- logo
no new introduced colours

```html
<!DOCTYPE html>
<html lang="en">
<head>
<meta charset="utf-8">
<title>Marlow Advisory Partners – Business Card</title>
<link rel="stylesheet" href="https://fonts.googleapis.com/css2?family=Arimo:wght@400;700&family=Roboto+Condensed:wght@400;700&display=swap">
<style>
  :root {
    --stage: #2b2b2d;
    --brand-blue: #1d3fa0;
    --brand-sky: #1aa3e0;
    --brand-magenta: #b0409c;
    --brand-green: #8cc63f;
    --card-white: #f4f4f5;
    --card-grey: #e6e6e8;
    --icon-grey: #8f9094;
    --text-blue: #1d3fa0;
  }
  * { margin: 0; padding: 0; box-sizing: border-box; }
  html, body {
    width: 1200px; height: 900px; overflow: hidden;
    background: var(--stage);
  }
  .canvas {
    position: relative; width: 1200px; height: 900px;
    display: flex; flex-direction: column; align-items: center;
    justify-content: center; gap: 36px;
  }
  .card {
    position: relative; width: 700px; height: 400px;
    border-radius: 4px; overflow: hidden;
    box-shadow: 0 14px 30px rgba(0,0,0,.45);
  }

  /* Back side */
  .card-back { background: var(--brand-blue); }
  .back-lockup {
    position: absolute; top: 36px; right: 44px;
    display: flex; align-items: center; gap: 12px;
  }
  .back-lockup .brand-mark {
    width: 22px; height: 22px; border-radius: 50%;
    background: var(--brand-sky); flex: none;
  }
  .back-lockup .brand-name {
    font-family: "Arimo", Arial, sans-serif; font-weight: 700;
    font-size: 22px; letter-spacing: .5px; text-transform: uppercase;
    color: var(--brand-sky); line-height: 1.2;
  }
  .colour-field {
    position: absolute; left: 0; right: 0; bottom: 0; height: 250px;
    background:
      linear-gradient(180deg, var(--brand-blue) 0%, rgba(29,63,160,0) 55%),
      linear-gradient(90deg, var(--brand-sky) 0%, var(--brand-sky) 22%, var(--brand-magenta) 50%, var(--brand-green) 82%, var(--brand-green) 100%);
    opacity: .9;
  }

  /* Front side */
  .card-front {
    background: linear-gradient(135deg, var(--card-white) 0%, var(--card-grey) 100%);
    font-family: "Arimo", Arial, sans-serif; color: var(--text-blue);
  }
  .holder {
    position: absolute; top: 44px; right: 44px;
    font-family: "Roboto Condensed", Arial, sans-serif;
  }
  .holder-name { font-weight: 700; font-size: 22px; letter-spacing: .3px; }
  .holder-role { font-weight: 400; font-size: 15px; margin-left: 4px; }

  .logo-lockup {
    position: absolute; top: 150px; left: 52px;
    display: flex; align-items: center; gap: 14px;
  }
  .logo-lockup .brand-mark {
    width: 26px; height: 26px; border-radius: 50%;
    background: var(--brand-blue); flex: none;
  }
  .logo-lockup .brand-name {
    font-weight: 700; font-size: 24px; line-height: 1.15;
    text-transform: uppercase; color: var(--brand-blue);
  }

  .contact-list {
    position: absolute; left: 370px; top: 238px;
    list-style: none; font-size: 16px;
  }
  .contact-list li {
    display: flex; align-items: center; gap: 12px; height: 30px;
  }
  .contact-list svg { width: 18px; height: 18px; fill: var(--icon-grey); flex: none; }
</style>
</head>
<body>
<main class="canvas">

  <section class="card card-back" aria-label="Card back">
    <div class="colour-field" role="img" aria-label="Large brand graphic in sky blue, magenta and green"></div>
    <div class="back-lockup">
      <span class="brand-mark"></span>
      <p class="brand-name">Marlow Advisory<br>Partners Pty Ltd</p>
    </div>
  </section>

  <section class="card card-front" aria-label="Card front">
    <p class="holder"><span class="holder-name">DANIEL HARTLEY</span><span class="holder-role">DIRECTOR</span></p>

    <div class="logo-lockup">
      <span class="brand-mark"></span>
      <p class="brand-name">Marlow Advisory<br>Partners Pty Ltd</p>
    </div>

    <ul class="contact-list">
      <li>
        <svg viewBox="0 0 24 24" aria-hidden="true"><path d="M12 2a7 7 0 0 0-7 7c0 5 7 13 7 13s7-8 7-13a7 7 0 0 0-7-7zm0 9.5A2.5 2.5 0 1 1 12 6.5a2.5 2.5 0 0 1 0 5z"/></svg>
        4/16 Kestrel St, Coogee. 2034
      </li>
      <li>
        <svg viewBox="0 0 24 24" aria-hidden="true"><path d="M7 1h10a2 2 0 0 1 2 2v18a2 2 0 0 1-2 2H7a2 2 0 0 1-2-2V3a2 2 0 0 1 2-2zm1 3v10h8V4H8zm1 12v2h2v-2H9zm4 0v2h2v-2h-2z"/></svg>
        0400 118 273
      </li>
      <li>
        <svg viewBox="0 0 24 24" aria-hidden="true"><path d="M2 5h20v14H2V5zm2 2v.5l8 5.5 8-5.5V7H4zm0 3v7h16v-7l-8 5.5L4 10z"/></svg>
        hello@marlowadvisory.com.au
      </li>
      <li>
        <svg viewBox="0 0 24 24" aria-hidden="true"><path d="M12 2a10 10 0 1 0 0 20 10 10 0 0 0 0-20zm6.9 9h-3a15 15 0 0 0-1.3-6A8 8 0 0 1 18.9 11zM12 4c.9 1.2 1.8 3.7 1.9 7h-3.8c.1-3.3 1-5.8 1.9-7zM9.4 5a15 15 0 0 0-1.3 6h-3A8 8 0 0 1 9.4 5zM5.1 13h3a15 15 0 0 0 1.3 6A8 8 0 0 1 5.1 13zM12 20c-.9-1.2-1.8-3.7-1.9-7h3.8c-.1 3.3-1 5.8-1.9 7zm2.6-1a15 15 0 0 0 1.3-6h3a8 8 0 0 1-4.3 6z"/></svg>
        www.marlowadvisory.com.au
      </li>
    </ul>
  </section>

</main>
</body>
</html>
```